MLD Illustration Web Design

Create illustration web design company for Mandirasa Luhur Digital (MLD). I more prefer design with illustration concept. Detail for requirement please see attach file. I'm also attach MLD logo. This logo had 2 type, 2D design and 3D design. You can chose one of them, or used both.
For the winner or had good design would be possible to private project to completeness this website
Attach file requirement is guidance for design, but any changes are welcome
Updates
Sorry, I forgot about contact. Please add menu contact. You can put this menu besides login menu or part of menu level #1, or put on some where to adjust your design. Menu contact will give pop up window to email MLD Company and Company Information (Address, Telephone, etc)
Target Market(s)
Company (Business To Business)
Industry/Entity Type
It Company
Look and feel
Each slider illustrates characteristics of the customer's brand and the style your logo design should communicate.

```html
<!DOCTYPE html>
<html lang="en">
<head>
<meta charset="utf-8">
<title>Mandirasa Luhur Digital — Software Development &amp; IT Consultant</title>
<link href="https://fonts.googleapis.com/css2?family=Roboto+Condensed:wght@300;400;700&display=swap" rel="stylesheet">
<style>
  :root {
    --teal: #80cdc1;
    --teal-soft: #8ad3c8;
    --bar: #333333;
    --nav-text: #9a9a9a;
    --white: #ffffff;
    --logo-green: #7aa832;
    --heading: #f2f2f2;
    --social: #6f7b7a;
  }
  * { margin: 0; padding: 0; box-sizing: border-box; }
  html, body { width: 1200px; height: 938px; overflow: hidden; }
  body {
    position: relative;
    background: var(--teal);
    font-family: "Roboto Condensed", "Arial Narrow", sans-serif;
  }
  .backdrop {
    position: absolute; left: 0; top: 64px; width: 1200px; height: 874px;
    background: radial-gradient(ellipse at 50% 55%, var(--teal-soft) 0%, var(--teal) 70%);
  }
  .topbar {
    position: absolute; left: 0; top: 0; width: 1200px; height: 64px;
    background: var(--bar);
  }
  .brand {
    position: absolute; left: 150px; top: 0; width: 154px; height: 64px;
    background: var(--white);
    display: flex; align-items: center; justify-content: center; gap: 8px;
  }
  .brand-dot { width: 26px; height: 26px; border-radius: 50%; background: var(--logo-green); }
  .brand-name { color: var(--logo-green); font-weight: 700; font-size: 34px; letter-spacing: 2px; }
  .main-nav {
    position: absolute; left: 623px; top: 24px;
    display: flex; gap: 19px; list-style: none;
  }
  .main-nav li {
    color: var(--nav-text); font-size: 13.5px; letter-spacing: 1px; text-transform: uppercase;
  }
  .hero-title {
    position: absolute; left: 0; width: 1200px; text-align: center;
    color: var(--heading); font-weight: 300; text-transform: uppercase;
    line-height: 1;
    text-shadow: 2px 3px 3px rgba(0,0,0,.28);
  }
  .hero-title.line-1 { top: 366px; font-size: 82px; }
  .hero-title.amp { top: 452px; font-size: 32px; }
  .hero-title.line-2 { top: 503px; font-size: 82px; }
  .scroll-down {
    position: absolute; left: 580px; top: 624px; width: 48px; height: 48px;
    border-radius: 50%; background: #f4f4f4;
    box-shadow: 0 2px 4px rgba(0,0,0,.25), inset 0 -3px 5px rgba(0,0,0,.1);
  }
  .scroll-down svg { position: absolute; left: 14px; top: 16px; }
  .service-icon {
    position: absolute; width: 154px; height: 142px; border-radius: 50%;
    border: 4px solid #e9e9e9;
    box-shadow: 0 3px 6px rgba(0,0,0,.25);
  }
  .service-icon.consulting { background: radial-gradient(circle at 50% 40%, #f4e24a 0 22%, #ffffff 45%, #e6e6e6 100%); }
  .service-icon.development { background: radial-gradient(circle at 60% 55%, #3a7fd0 0 22%, #9fc4e8 35%, #ffffff 55%, #e6e6e6 100%); }
  .service-icon.process { background: radial-gradient(circle at 50% 50%, #f2a70b 0 24%, #ffffff 45%, #e6e6e6 100%); }
  .service-label {
    position: absolute; top: 870px; width: 160px; text-align: center;
    color: var(--white); font-weight: 700; font-size: 23px; line-height: 1;
    text-shadow: 1px 2px 3px rgba(0,0,0,.35);
  }
  .social { position: absolute; top: 892px; display: flex; gap: 13px; left: 82px; }
  .social span {
    width: 28px; height: 28px; border-radius: 50%; background: var(--social);
    color: #e8e8e8; font-size: 14px; font-weight: 700;
    display: flex; align-items: center; justify-content: center;
  }
</style>
</head>
<body>
  <div class="backdrop" role="img" aria-label="Decorative geometric background pattern"></div>

  <header class="topbar">
    <div class="brand"><span class="brand-dot"></span><span class="brand-name">MLD</span></div>
    <ul class="main-nav">
      <li>Services</li><li>Products</li><li>Clients</li><li>Company</li><li>Blog</li><li>Contact</li>
    </ul>
  </header>

  <h1 class="hero-title line-1">Software Development</h1>
  <div class="hero-title amp">&amp;</div>
  <div class="hero-title line-2">IT Consultant</div>

  <div class="scroll-down">
    <svg width="20" height="16" viewBox="0 0 20 16"><polyline points="2,4 10,12 18,4" fill="none" stroke="#5fb5a8" stroke-width="4"/></svg>
  </div>

  <div class="service-icon consulting" style="left:335px; top:722px;" role="img" aria-label="Light bulb illustration for consulting"></div>
  <div class="service-icon development" style="left:502px; top:714px;" role="img" aria-label="Computer monitor and globe illustration for development"></div>
  <div class="service-icon process" style="left:668px; top:714px;" role="img" aria-label="Gear with tick illustration for process"></div>

  <div class="service-label" style="left:331px;">Consulting</div>
  <div class="service-label" style="left:500px;">Development</div>
  <div class="service-label" style="left:667px;">Process</div>

  <div class="social"><span>S</span><span>C</span></div>
</body>
</html>
```